Pet and Potrait photography business needs web site design

I need a web design that is for a portrait and pet photography business based in Tasmania, Australia. It is a small, simple concept, photography business that focuses on portraits and pet photography only. I need something that is clean, maybe a white background, fun, and appealing to families. The design must make my images stand out and be the focus. The final design needs to show that it is aimed a families, pet owners, and is all about the clients - albeit the two or four legged kinds.

Business name is: reed and willow photography

I need it to be able to have the following:

- Include space for logo design which is also through SketchHarbor
- Home Page which has a gallery of my images (which you can click an arrow - either forward or back - that showcases my images
- About Page
- Portfolio Page (preferably two a) for portraits, and b) for pet photography
- Pricing page
- secure log in client page
- Contact page

Reason: Waiting for logo design to be completed to fit in with overall website design.

Target Market(s)

Families
Pet owners
Single couples who have fur babies

Industry/Entity Type

Business

Font styles to use
Serif
Decorative
Script

Colors

Designer to choose colors to be used in the design.

Requirements
Must have
• the website must provide the ability for me to upload and change images regularly.
Nice to have
• Logo design is a secondary project that will need to be worked on as well. I will pay an additional amount for those that are prepared to include this in the project.
Should not have
• No graffiti style writing.
It has to be elegant, and stylish and be aimed at females.
Women are going to be the driver for having portraits done of either their babies, children, or fur babies - i.e. pets.

```html
<!DOCTYPE html>
<html lang="en">
<head>
<meta charset="utf-8">
<title>Reed and Willow Photography</title>
<link rel="stylesheet" href="https://fonts.googleapis.com/css2?family=Noto+Serif:ital,wght@0,400;1,400&family=Open+Sans:wght@400;600;700&display=swap">
<style>
:root{
  --green:#a5c84a;
  --green-deep:#7fa82c;
  --green-bar:rgba(150,190,50,.88);
  --ink:#3d3d3d;
  --muted:#7a7a7a;
  --soft:#efefeb;
  --rule:#cfcfcf;
  --dark:#3b3b3b;
  --white:#ffffff;
}
*{margin:0;padding:0;box-sizing:border-box}
html,body{width:886px;height:1200px;overflow:hidden;background:var(--white)}
body{position:relative;font-family:"Open Sans",Arial,sans-serif;color:var(--ink)}
.abs{position:absolute}

/* header */
.brand{left:94px;top:20px;width:130px;text-align:center}
.brand-mark{display:block;width:14px;height:14px;background:var(--green-deep);margin:0 auto 5px}
.brand-name{font-family:"Open Sans",sans-serif;font-weight:600;color:var(--green-deep);font-size:10.5px;letter-spacing:.5px;line-height:1.2;text-transform:uppercase;white-space:nowrap}
.brand-sub{font-size:6.5px;letter-spacing:2.6px;color:var(--green-deep);font-weight:600;text-transform:uppercase}
.nav{top:32px;left:375px;display:flex;align-items:center;height:26px}
.nav a{font-size:9.5px;letter-spacing:1.6px;color:var(--ink);text-decoration:none;text-transform:uppercase;padding:0 8px;line-height:26px}
.nav a.active{background:var(--green);color:var(--white)}
.nav .gap{margin-left:7px}

/* hero */
.hero{left:81px;top:86px;width:723px;height:274px;border-top:4px solid #bdbdb4;
  background:radial-gradient(ellipse at 38% 45%,#f0cdb6 0%,#e0b48e 30%,#d8c086 60%,#c8c57a 100%)}
.hero-card{left:496px;top:42px;width:196px;height:160px;background:rgba(165,200,74,.92);text-align:center;color:var(--white);font-family:"Noto Serif",Georgia,serif;font-style:italic}
.hero-card h1{font-weight:400;font-size:34px;line-height:36px;margin-top:28px}
.hero-card p{font-size:12px;margin-top:-2px}
.hero-card .cta{display:block;width:146px;height:22px;margin:14px auto 0;background:var(--white);color:var(--ink);font-size:13.5px;line-height:22px;border:1px solid #d9d9d9}
.hero-bar{left:0;bottom:0;width:100%;height:24px;background:var(--green-bar);color:var(--white);font-family:"Noto Serif",Georgia,serif;font-style:italic;font-size:9.5px;line-height:24px;padding-left:29px}
.pager{right:76px;top:0;display:flex;align-items:center;gap:5px;height:24px;font-style:normal;font-size:12px}
.dot{width:9px;height:9px;border-radius:50%;background:rgba(255,255,255,.45)}
.dot.on{background:var(--white)}

.tagline{left:81px;top:378px;width:723px;text-align:center;font-family:"Noto Serif",Georgia,serif;font-style:italic;font-size:15.5px;color:var(--ink)}
.tag-rule{left:81px;top:425px;width:723px;height:2px;background:#e2e2e2;box-shadow:0 1px 1px #ddd}

/* galleries */
.label{font-size:9.5px;font-weight:400;letter-spacing:1.8px;color:var(--muted);text-transform:uppercase}
.strip{display:flex;gap:2px;width:662px;height:157px}
.strip .shot{flex:1}
.arrow{width:26px;height:115px}

/* info */
.info{left:81px;top:934px;width:723px;height:226px;background:var(--soft)}
.col{top:30px;width:150px}
.col h2{font-size:8.5px;font-weight:700;letter-spacing:.8px;text-transform:uppercase;color:var(--ink);margin-bottom:10px}
.col p{font-family:"Noto Serif",Georgia,serif;font-style:italic;font-size:9.2px;line-height:14.7px;color:var(--muted)}
.col p.dark{color:var(--ink)}
.col .more{display:block;margin-top:3px;font-size:9px;color:var(--ink);text-decoration:none}
.touch{display:block;width:138px;height:21px;margin-top:23px;background:var(--dark);color:var(--white);text-align:center;font-family:"Noto Serif",Georgia,serif;font-style:italic;font-size:13px;line-height:21px;border-radius:2px}
.divider{left:111px;top:922px;width:662px;height:4px;background:#dedede}

.footer{left:81px;top:1160px;width:723px;height:40px;background:var(--dark);color:#bdbdbd;font-family:"Noto Serif",Georgia,serif;font-style:italic;font-size:8.5px}
.footer .copy{left:30px;top:14px}
.footer .mini{left:518px;top:8px;font-size:11px;line-height:1;color:#cfcfcf;white-space:nowrap}
.footer .mini small{display:block;font-size:6.5px;margin-top:1px}
.social{right:40px;top:10px;display:flex;gap:9px}
.social span{width:19px;height:19px;border-radius:50%;background:#5a5a5a}
</style>
</head>
<body>

<header>
  <div class="abs brand">
    <span class="brand-mark"></span>
    <div class="brand-name">Reed and Willow</div>
    <div class="brand-sub">Photography</div>
  </div>
  <nav class="abs nav">
    <a class="active" href="#">Home</a>
    <a class="gap" href="#">About</a>
    <a class="gap" href="#">Portfolio</a>
    <a class="gap" href="#">Pricing</a>
    <a href="#">Login</a>
    <a class="gap" href="#">Contact</a>
  </nav>
</header>

<section class="abs hero" role="img" aria-label="Close portrait of a smiling young girl in a sunlit field">
  <div class="abs hero-card">
    <h1>Beautiful<br>Portraits</h1>
    <p>Make Beautiful Memories</p>
    <span class="cta">View Pricing</span>
  </div>
  <div class="abs hero-bar">Hendrerit ante nullam malesuada massa eget nisl rutrum ac hendrerit ante fermentum.
    <div class="abs pager"><span>&laquo;</span><span class="dot on"></span><span class="dot"></span><span class="dot"></span><span class="dot"></span><span>&raquo;</span></div>
  </div>
</section>

<p class="abs tagline">Fresh, Clean, Honest Portrait Photography For The Best Possible Results</p>
<div class="abs tag-rule"></div>

<h3 class="abs label" style="left:111px;top:466px">Portrait Gallery</h3>
<svg class="abs arrow" style="left:84px;top:522px" viewBox="0 0 26 115"><polyline points="24,0 2,57 24,115" fill="none" stroke="#c9c9c9" stroke-width="1.2"/></svg>
<div class="abs strip" style="left:111px;top:499px">
  <div class="shot" role="img" aria-label="Smiling girl among dune grasses" style="background:linear-gradient(160deg,#c9d6d8,#d9c3a4 55%,#7a8a5c)"></div>
  <div class="shot" role="img" aria-label="Two sisters hugging on the beach" style="background:linear-gradient(180deg,#e3c7a2 0%,#d6b48d 58%,#a9c852 58%,#9cc24a 100%);position:relative">
    <svg width="100%" height="100%" viewBox="0 0 219 157" style="position:absolute;inset:0"><path d="M109.5 88v28M95.5 102h28" stroke="#fff" stroke-width="1.2"/></svg>
  </div>
  <div class="shot" role="img" aria-label="Young girl crouching in tall beach grass" style="background:linear-gradient(170deg,#e7ebe9,#c9b98e 50%,#9e9462)"></div>
</div>
<svg class="abs arrow" style="left:776px;top:522px" viewBox="0 0 26 115"><polyline points="2,0 24,57 2,115" fill="none" stroke="#c9a9cf" stroke-width="1.2"/></svg>

<h3 class="abs label" style="left:111px;top:695px">Pets Gallery</h3>
<svg class="abs arrow" style="left:84px;top:751px" viewBox="0 0 26 115"><polyline points="24,0 2,57 24,115" fill="none" stroke="#c9c9c9" stroke-width="1.2"/></svg>
<div class="abs strip" style="left:111px;top:728px">
  <div class="shot" role="img" aria-label="Two kittens on a terracotta rooftop" style="background:linear-gradient(150deg,#7c8a8e,#b9a9a0 50%,#c98e7e)"></div>
  <div class="shot" role="img" aria-label="Black dog lying beside a log on a path" style="background:linear-gradient(180deg,#4d6a3a,#8a7d6a 55%,#9a8672)"></div>
  <div class="shot" role="img" aria-label="White fluffy dog on a black background" style="background:radial-gradient(ellipse at 60% 55%,#e8e8e8 0%,#bcbcbc 30%,#000 60%)"></div>
</div>
<svg class="abs arrow" style="left:776px;top:751px" viewBox="0 0 26 115"><polyline points="2,0 24,57 2,115" fill="none" stroke="#c9c9c9" stroke-width="1.2"/></svg>

<div class="abs divider"></div>

<section class="abs info">
  <div class="abs col" style="left:29px">
    <h2>Simpler Than Ever</h2>
    <p>Lorem ipsum dolor sit amet, consectetur adipiscing elit. Nullam malesuada massa eget nisl rutrum ac hendrerit ante fermentum. Vestibulum ante ipsum primis in faucibus orci luctus et ultrices posuere cubilia Curae.</p>
    <a class="more" href="#">Learn More &raquo;</a>
  </div>
  <div class="abs col" style="left:201px">
    <h2>Impressive Portraits</h2>
    <p>Nullam malesuada massa eget nisl rutrum ac hendrerit ante fermentum. Vestibulum ante ipsum primis in faucibus orci luctus et ultrices posuere cubilia Curae. Lorem ipsum dolor sit amet, consectetur adipiscing.</p>
    <a class="more" href="#">See Portrait Gallery &raquo;</a>
  </div>
  <div class="abs col" style="left:375px">
    <h2>From The Blog</h2>
    <p>Lorem ipsum dolor sit amet, consectetur adipiscing elit.<br><br>Nullam malesuada massa eget nisl rutrum ac hendrerit ante.<br><br>Vestibulum ante ipsum primis in faucibus orci.</p>
    <a class="more" href="#">View All &raquo;</a>
  </div>
  <div class="abs col" style="left:545px;width:170px">
    <h2>Contact Us</h2>
    <p class="dark">Phone: +61 3 6200 4418<br>Fax: +61 3 6200 4419<br>Email: info@reedandwillow.com<br>L.N Some Streat Unknown<br>Location Of The Place<br>City - City Name<br>The Country</p>
    <span class="touch">Get In Touch</span>
  </div>
</section>

<footer class="abs footer">
  <span class="abs copy">&copy; Copyright - reed &amp; willow Photography</span>
  <span class="abs mini">reed&amp;willow<small>Photography</small></span>
  <div class="abs social"><span></span><span></span><span></span></div>
</footer>

</body>
</html>
```